cover for CD- Single.

This design is for a CD cover. The design is at your disposal, using all of your creative talents.
Things to improve the photo: Cleaning the face, removing blemishes.
Design in black and white would be an option (Color would be another option). I reiterate it is up to your taste and criteria, any reform and art on the cover of Cd.
Name of the single: El Camino del Alba Serena
Artist Name: Marisol Quenteva

Target Market(s)

Single Music

Industry/Entity Type

Music

Colors

Designer to choose colors to be used in the design.

Requirements
Must have
• style, elegance, professionalism, spontaneity
Nice to have
• I want it to be as professional as possible.
Should not have
• Spelling errors.

```html
<!DOCTYPE html>
<html lang="es">
<head>
<meta charset="UTF-8">
<title>El Camino del Alba Serena — Marisol Quenteva</title>
<link href="https://fonts.googleapis.com/css2?family=Montserrat:wght@700&family=Sacramento&display=swap" rel="stylesheet">
<style>
  :root {
    --backdrop: #d6d6d8;
    --ink: #000000;
    --paper: #ffffff;
    --photo-light: #d9d9d9;
    --photo-dark: #4a4a4a;
  }
  * { margin: 0; padding: 0; box-sizing: border-box; }
  html, body {
    width: 1200px;
    height: 561px;
    overflow: hidden;
    background: var(--backdrop);
  }
  .cover {
    position: absolute;
    left: 366px;
    top: 46px;
    width: 468px;
    height: 468px;
    background: var(--paper);
    overflow: hidden;
  }
  .cover__band {
    position: absolute;
    left: 0;
    top: 0;
    width: 100%;
    height: 246px;
    background: var(--ink);
  }
  .cover__photo {
    position: absolute;
    left: 125px;
    top: 158px;
    width: 221px;
    height: 229px;
    background: linear-gradient(135deg, var(--photo-light) 0%, #a8a8a8 45%, var(--photo-dark) 100%);
  }
  .cover__lines {
    position: absolute;
    left: 0;
    top: 0;
    width: 468px;
    height: 468px;
  }
  .title__lead {
    position: absolute;
    left: 0;
    top: 22px;
    width: 100%;
    text-align: center;
    font-family: "Montserrat", sans-serif;
    font-weight: 700;
    font-size: 26px;
    color: var(--paper);
    letter-spacing: 0.2px;
  }
  .title__script {
    position: absolute;
    left: 0;
    top: 52px;
    width: 100%;
    text-align: center;
    font-family: "Sacramento", cursive;
    font-size: 92px;
    line-height: 1.2;
    color: var(--paper);
    z-index: 2;
  }
  .artist {
    position: absolute;
    left: 0;
    top: 402px;
    width: 100%;
    text-align: center;
    font-family: "Montserrat", sans-serif;
    font-weight: 700;
    font-size: 23px;
    color: var(--ink);
    letter-spacing: 0.5px;
    white-space: nowrap;
  }
  .artist__initial {
    font-family: "Sacramento", cursive;
    font-weight: 400;
    font-size: 46px;
    margin-right: -2px;
    vertical-align: -4px;
  }
  .artist__gap { display: inline-block; width: 12px; }
</style>
</head>
<body>
  <main class="cover">
    <div class="cover__band"></div>
    <div class="cover__photo" role="img" aria-label="Black and white portrait of the artist with eyes closed, hand touching her hair"></div>
    <svg class="cover__lines" viewBox="0 0 468 468" aria-hidden="true">
      <line x1="310" y1="174" x2="371" y2="174" stroke="#ffffff" stroke-width="1.5"/>
      <line x1="361" y1="174" x2="361" y2="245" stroke="#ffffff" stroke-width="1.5"/>
      <line x1="115" y1="288" x2="115" y2="383" stroke="#000000" stroke-width="1.5"/>
      <line x1="102" y1="377" x2="166" y2="377" stroke="#000000" stroke-width="1.5"/>
    </svg>
    <h1 class="title">
      <span class="title__lead">El Camino del</span>
      <span class="title__script">Alba Serena</span>
    </h1>
    <p class="artist"><span class="artist__initial">M</span>ARISOL<span class="artist__gap"></span><span class="artist__initial">Q</span>UENTEVA</p>
  </main>
</body>
</html>
```